Bref créative
Stationary (Branding) for Plumbing & Heating Buisness
Dorrick Haines Ltd
Use same font as used in my logo
Dorrick Haines
Unit 8 Larchmoor Ind Est.
Cwmbrellog
Pontypool
Torfaen
dorrick@greenvoltaria.co.uk
www.dorrickhaines.com
Looking for complete stationary with A4 letter head, business cards and so on using the logo provided. Modern, clean and eco friendly is the image we are looking for.
The font used in the logo is not final and maybe changed so please ignore that.
Would like to see the logo on the back of the card with spot UV effect.
The font in this logo is not final and may change
plumbing
renewables
heating

```html
<!DOCTYPE html>
<html lang="en">
<head>
<meta charset="utf-8">
<title>Dorrick Haines Ltd – Stationery</title>
<link rel="stylesheet" href="https://fonts.googleapis.com/css2?family=Open+Sans:wght@400;600;700&display=swap">
<style>
:root{
  --bg:#3a3b3d;
  --paper:#ffffff;
  --ink:#4a4a4a;
  --muted:#9a9a9a;
  --green:#6cb02a;
  --blue:#1d5dab;
  --blue-dark:#123f7a;
  --red:#d9402b;
  --card-dark:#1f2021;
  --sign:#c9d3dc;
}
*{margin:0;padding:0;box-sizing:border-box}
html,body{width:1200px;height:354px;overflow:hidden}
body{background:var(--bg);font-family:"Open Sans",Arial,sans-serif;position:relative;color:var(--ink)}
.item{position:absolute;background:var(--paper);box-shadow:0 2px 6px rgba(0,0,0,.45);overflow:hidden}
.label{position:absolute;font-size:6px;color:var(--muted);text-align:center}
.brand{display:flex;align-items:center;gap:4px}
.brand-dot{width:10px;height:10px;border-radius:50%;background:var(--green);flex:none}
.brand-name{font-weight:700;color:var(--green);font-size:7px;white-space:nowrap}
.wave{position:absolute;left:0;bottom:0;width:100%}
/* left showcase */
.showcase-logo{position:absolute;left:24px;top:112px}
.showcase-logo .brand-dot{width:22px;height:22px}
.showcase-logo .brand-name{font-size:15px;color:#fff}
.showcase-logo .tagline{font-size:8px;color:var(--muted);margin:2px 0 0 26px;letter-spacing:.5px}
.card-front{left:24px;top:172px;width:130px;height:74px}
.card-front .brand{position:absolute;left:8px;top:8px}
.card-front .person{position:absolute;left:8px;top:26px;font-size:5px;line-height:1.5}
.card-front .person b{font-size:6px;color:var(--blue)}
.card-back{left:24px;top:256px;width:130px;height:74px;background:var(--card-dark)}
.card-back .brand{position:absolute;left:24px;top:30px}
.card-back .brand-name{font-size:9px}
/* letterhead */
.letterhead{top:14px;width:150px;height:316px}
.letterhead .brand{position:absolute;right:10px;top:12px}
.letterhead .watermark{position:absolute;left:35px;top:110px;width:80px;height:80px;border-radius:50%;background:var(--green);opacity:.07}
.letter-text{position:absolute;left:12px;right:12px;top:44px;font-size:3.6px;line-height:1.6}
.letter-text p{margin-bottom:4px}
.signature{width:40px;height:10px;background:var(--sign);margin:3px 0}
.letter-foot{position:absolute;left:0;right:0;bottom:6px;text-align:center;font-size:3.4px;color:#fff;z-index:2}
.lh-1{left:252px}.lh-2{left:415px}
/* compliment slip */
.slip{left:636px;top:196px;width:130px;height:108px}
.slip .brand{position:absolute;left:10px;top:12px}
.slip .addr{position:absolute;left:10px;top:30px;font-size:4px;line-height:1.5}
/* envelopes */
.env-front{left:790px;top:196px;width:140px;height:108px}
.env-front .brand{position:absolute;left:10px;top:10px}
.env-front .addr{position:absolute;left:10px;top:26px;font-size:4px;line-height:1.5}
.env-back{left:955px;top:96px;width:200px;height:96px;background:#eef2f6}
.env-dl{left:955px;top:204px;width:200px;height:96px}
.env-dl .brand{position:absolute;left:10px;top:10px}
.env-dl .addr{position:absolute;left:10px;top:25px;font-size:4px;line-height:1.5}
</style>
</head>
<body>

<div class="showcase-logo">
  <div class="brand"><span class="brand-dot"></span><span class="brand-name">Dorrick Haines Ltd</span></div>
  <div class="tagline">plumbing · heating · renewables</div>
</div>

<div class="item card-front">
  <div class="brand"><span class="brand-dot"></span><span class="brand-name">Dorrick Haines Ltd</span></div>
  <div class="person"><b>Dorrick Haines</b><br>Managing Director<br>Unit 8 Larchmoor Ind Est.<br>Cwmbrellog, Pontypool, Torfaen<br>dorrick@greenvoltaria.co.uk<br>www.dorrickhaines.com</div>
  <svg class="wave" viewBox="0 0 130 20" preserveAspectRatio="none" height="16"><path d="M0 12 Q55 0 130 9 L130 20 L0 20Z" fill="var(--blue)"/><path d="M0 16 Q60 6 130 13 L130 20 L0 20Z" fill="var(--green)"/></svg>
</div>

<div class="item card-back">
  <div class="brand"><span class="brand-dot"></span><span class="brand-name">Dorrick Haines Ltd</span></div>
</div>

<div class="item letterhead lh-1">
  <div class="brand"><span class="brand-dot"></span><span class="brand-name">Dorrick Haines Ltd</span></div>
  <div class="watermark"></div>
  <div class="letter-text">
    <p>12 March 2024</p>
    <p>Dear Customer</p>
    <p>Thank you for choosing us for your new heating system. Our engineers will visit next week to survey the property and agree a plan that keeps your home warm and efficient.</p>
    <p>We fit boilers, solar panels and heat pumps across the valleys, and every job carries our full workmanship guarantee.</p>
    <p>Yours sincerely</p>
    <div class="signature" role="img" aria-label="Handwritten signature"></div>
    <p>Dorrick Haines</p>
  </div>
  <div class="letter-foot">Unit 8 Larchmoor Ind Est. · Cwmbrellog · Pontypool · Torfaen · www.dorrickhaines.com</div>
  <svg class="wave" viewBox="0 0 150 40" preserveAspectRatio="none" height="34"><path d="M0 18 Q65 0 150 14 L150 40 L0 40Z" fill="var(--blue)"/><path d="M0 26 Q70 10 150 22 L150 40 L0 40Z" fill="var(--green)"/><path d="M0 22 Q68 5 150 18" stroke="var(--red)" stroke-width="1" fill="none"/></svg>
</div>

<div class="item letterhead lh-2">
  <div class="brand"><span class="brand-dot"></span><span class="brand-name">Dorrick Haines Ltd</span></div>
  <div class="watermark"></div>
  <div class="letter-text">
    <p>Dear Customer</p>
    <p>Thank you for choosing us for your new heating system. Our engineers will visit next week to survey the property and agree a plan that keeps your home warm and efficient.</p>
    <p>We fit boilers, solar panels and heat pumps across the valleys, and every job carries our full workmanship guarantee.</p>
    <p>Yours sincerely</p>
    <div class="signature" role="img" aria-label="Handwritten signature"></div>
    <p>Dorrick Haines</p>
  </div>
  <div class="letter-foot">dorrick@greenvoltaria.co.uk · www.dorrickhaines.com</div>
  <svg class="wave" viewBox="0 0 150 40" preserveAspectRatio="none" height="34"><path d="M0 18 Q65 0 150 14 L150 40 L0 40Z" fill="var(--blue)"/><path d="M0 26 Q70 10 150 22 L150 40 L0 40Z" fill="var(--green)"/><path d="M0 22 Q68 5 150 18" stroke="var(--red)" stroke-width="1" fill="none"/></svg>
</div>
<div class="label" style="left:252px;top:336px;width:150px">Letterhead 1</div>
<div class="label" style="left:415px;top:336px;width:150px">Letterhead 2</div>

<div class="item slip">
  <div class="brand"><span class="brand-dot"></span><span class="brand-name">Dorrick Haines Ltd</span></div>
  <div class="addr">Unit 8 Larchmoor Ind Est.<br>Cwmbrellog, Pontypool<br>Torfaen<br>www.dorrickhaines.com</div>
  <svg class="wave" viewBox="0 0 130 30" preserveAspectRatio="none" height="22"><path d="M0 14 Q55 0 130 10 L130 30 L0 30Z" fill="var(--blue)"/><path d="M0 20 Q60 8 130 16 L130 30 L0 30Z" fill="var(--green)"/></svg>
</div>
<div class="label" style="left:636px;top:310px;width:130px">Compliment Slip</div>

<div class="item env-front">
  <div class="brand"><span class="brand-dot"></span><span class="brand-name">Dorrick Haines Ltd</span></div>
  <div class="addr">Unit 8 Larchmoor Ind Est.<br>Cwmbrellog, Pontypool, Torfaen</div>
  <svg class="wave" viewBox="0 0 140 30" preserveAspectRatio="none" height="22"><path d="M0 14 Q60 0 140 10 L140 30 L0 30Z" fill="var(--blue)"/><path d="M0 20 Q65 8 140 16 L140 30 L0 30Z" fill="var(--green)"/></svg>
</div>
<div class="label" style="left:790px;top:310px;width:140px">Envelope</div>

<div class="item env-back">
  <svg width="200" height="96" viewBox="0 0 200 96"><path d="M0 0 L100 52 L200 0Z" fill="var(--blue)"/><path d="M0 0 L100 46 L200 0" fill="none" stroke="var(--blue-dark)" stroke-width="2"/><path d="M0 96 L100 50 L200 96" fill="none" stroke="#d5dce3" stroke-width="1"/></svg>
</div>
<div class="item env-dl">
  <div class="brand"><span class="brand-dot"></span><span class="brand-name">Dorrick Haines Ltd</span></div>
  <div class="addr">Unit 8 Larchmoor Ind Est.<br>Cwmbrellog, Pontypool, Torfaen</div>
</div>
<div class="label" style="left:955px;top:306px;width:200px">DL Envelope</div>

</body>
</html>
```